Email Signature

We are looking for creative email signature for our company. Please find attached the logo of our company for your reference. now we understand there isn't much can be done with email signature but we are looking for out of the box designs. Nothing specific in mind

Please insert fake numbers, website and/or address, etc just to showcase the designs. once the design is chosen we will provide the actual details.
Updates

Dear All,

We wouldlike to extend our apology for not being able to provide feedbacks to everysingle design. We were extremely busy and we have multiple contests opensimultaneously which makes the process harder. However, thank you all for theefforts you have put into this contest. We have received anoverwhelming quality responses & it has been a very difficult task tochoose just one, we easily Loved at least several designs...

Thanksagain for participating, we wish you all success in your design ventures.

Kindregards,

KLC Team

Industry/Entity Type

It Company

```html
<!DOCTYPE html>
<html lang="en">
<head>
<meta charset="utf-8">
<title>Trade Nest – Email Signature</title>
<link rel="stylesheet" href="https://fonts.googleapis.com/css2?family=Arimo:ital,wght@0,400;0,700;1,400&display=swap">
<style>
  :root {
    --brand-blue: #3d8ef0;
    --brand-green: #66e619;
    --ink: #111111;
    --rule: #7a7a7a;
    --paper: #ffffff;
  }
  * { margin: 0; padding: 0; box-sizing: border-box; }
  html, body {
    width: 1200px;
    height: 1000px;
    overflow: hidden;
    background: var(--paper);
    font-family: "Arimo", Arial, sans-serif;
  }
  .signature {
    position: relative;
    width: 1200px;
    height: 1000px;
  }
  .wordmark {
    position: absolute;
    left: 335px;
    top: 420px;
    width: 320px;
    text-align: center;
    font-size: 58px;
    font-weight: 700;
    letter-spacing: -2px;
    color: var(--brand-blue);
    line-height: 1;
    white-space: nowrap;
  }
  .social-links {
    position: absolute;
    left: 592px;
    top: 574px;
    display: flex;
    align-items: center;
    gap: 8px;
  }
  .social-dot {
    width: 12px;
    height: 12px;
    background: var(--brand-green);
  }
  .divider {
    position: absolute;
    left: 671px;
    top: 341px;
    width: 1px;
    height: 252px;
    background: var(--rule);
  }
  .details {
    position: absolute;
    left: 687px;
    top: 341px;
    font-size: 16px;
    line-height: 19.3px;
    color: var(--ink);
    white-space: nowrap;
  }
  .details .name {
    font-size: 19px;
    font-weight: 700;
    color: var(--brand-blue);
    line-height: 22px;
  }
  .details .role {
    font-style: italic;
    color: var(--brand-green);
  }
  .details .block { margin-top: 19.3px; }
  .details .label { color: var(--brand-green); margin-right: 4px; }
  .details .link { color: var(--brand-blue); text-decoration: none; display: block; }
</style>
</head>
<body>
<div class="signature">
  <div class="wordmark">TradeNest</div>

  <div class="social-links">
    <span class="social-dot" aria-label="Social profile"></span>
    <span class="social-dot" aria-label="Social profile"></span>
    <svg width="19" height="13" viewBox="0 0 19 13" aria-label="Email">
      <rect x="0" y="0" width="19" height="13" fill="var(--brand-green)"/>
      <path d="M0.5 0.8 L9.5 7.5 L18.5 0.8 M0.5 12.2 L7 6 M18.5 12.2 L12 6" fill="none" stroke="#ffffff" stroke-width="1.1"/>
    </svg>
  </div>

  <div class="divider"></div>

  <div class="details">
    <div class="name">Trade Nest</div>
    <div class="role">Occupation</div>

    <div class="block">
      <div><span class="label">Tel.:</span> 418-730-2941</div>
      <div><span class="label">Fax:</span> 418-730-2941</div>
      <div><span class="label">Office:</span> 418-730-2947</div>
    </div>

    <div class="block">
      <div>1847 West Harbor Rd</div>
      <div>P.O. Box 3172</div>
      <div>Lakeview,&nbsp; USA 4821</div>
    </div>

    <div class="block">
      <a class="link" href="mailto:mail@tradenestco.com">mail@tradenestco.com</a>
      <a class="link" href="#">www.tradenest.com</a>
    </div>
  </div>
</div>
</body>
</html>
```